STI/STD Medical Clinic- Wellspring Crest Partners, Inc Website

We are a STI clinic in florida looking for a website. We want to be professional but also playful. We want a buildout similar to the website listed below as our clinic is very similar to theirs.

This is a great example of a clinic doing similar stuff as us. We obviously do not want their color scheme but their format and buildout work. Please see our logo attached for color schemes etc.

https://bluefernclinicmiami.org

Industry/Entity Type

Medical

Coding

Coded - Design and coding required

Number of Pages Required

5+ page

Font styles to use
Sans Serif

```html
<!DOCTYPE html>
<html lang="en">
<head>
<meta charset="utf-8">
<title>Wellspring Crest Partners, Inc</title>
<link rel="stylesheet" href="https://fonts.googleapis.com/css2?family=Lato:wght@400;700;900&display=swap">
<style>
:root{
  --primary:#5433e0;
  --primary-bright:#2f5cf0;
  --violet:#6a3de8;
  --ink:#111018;
  --text:#2a2833;
  --muted:#9a98a6;
  --line:#3a3845;
  --lilac-bg:#f3f1fd;
  --lavender:#e3ddfa;
  --field:#f5f3fd;
  --pink-tile:#f9c9ef;
  --pink-text:#e044c8;
  --peach-tile:#fcc6c0;
  --peach-text:#ef5248;
  --lav-tile:#d9c9f8;
  --lav-text:#6a40d8;
  --link-blue:#6fb5f5;
  --star:#f0524a;
  --white:#ffffff;
}
*{box-sizing:border-box;margin:0;padding:0}
html,body{width:1200px;height:3509px;overflow:hidden}
body{position:relative;background:var(--white);font-family:'Lato',sans-serif;color:var(--text)}
.abs{position:absolute}
a{color:inherit;text-decoration:none}

/* hero */
.hero-bg{left:0;top:0;width:1200px;height:637px;background:linear-gradient(115deg,#fbeefa 0%,#f4c8ef 45%,#d8b8f2 75%,#c7b6f4 100%)}
.brand{font-weight:900;font-size:22px;color:var(--primary);display:flex;align-items:center;gap:10px}
.brand-dot{width:26px;height:26px;border-radius:50%;background:var(--pink-text)}
.nav{top:36px;left:534px;display:flex;gap:20px;font-size:14.5px;color:#5d5b68}
.nav .active{color:var(--ink);font-weight:700;border-bottom:2px solid var(--ink);padding-bottom:3px}
.btn{display:flex;align-items:center;justify-content:center;border-radius:6px;font-weight:700;font-size:15.5px;color:var(--white);background:var(--primary)}
.nav-contact{left:963px;top:26px;width:120px;height:42px;background:linear-gradient(90deg,var(--primary-bright),var(--primary));font-size:15px}
.hero-title{left:117px;top:180px;font-weight:900;font-size:58px;line-height:68px;color:var(--ink);letter-spacing:-0.5px}
.hero-title span{color:var(--violet)}
.hero-text{left:117px;top:336px;width:390px;font-size:16.5px;line-height:25px;color:#8f8a9c}
.hero-btn{left:117px;top:404px;width:218px;height:56px;font-size:15.5px;text-transform:uppercase}
.hero-photo{left:640px;top:136px;width:412px;height:420px;border-radius:206px 206px 0 0;background:radial-gradient(circle at 50% 40%,#f0d3c6 0 22%,transparent 23%),linear-gradient(180deg,#e98ae5 0%,#b57ee9 60%,#7f8bf0 100%)}
.deco-circle{left:831px;top:518px;width:490px;height:490px;border-radius:50%;background:var(--lavender)}

/* services card */
.services{left:117px;top:556px;width:966px;height:222px;background:var(--white);border-radius:27px;box-shadow:0 10px 30px rgba(90,60,180,.08)}
.services h2{position:absolute;left:53px;top:56px;font-size:30px;font-weight:700;color:var(--ink)}
.services p{position:absolute;left:53px;top:100px;width:310px;font-size:13.5px;line-height:22px;color:var(--muted)}
.tile{top:50px;width:98px;height:118px;border-radius:6px;display:flex;flex-direction:column;align-items:center;justify-content:flex-end;padding-bottom:14px;font-size:15.5px;gap:14px}
.tile svg{width:44px;height:44px}
.tile-prep{left:489px;background:var(--pink-tile);color:var(--pink-text)}
.tile-hep{left:608px;background:var(--peach-tile);color:var(--peach-text)}
.tile-hiv{left:726px;background:var(--lav-tile);color:var(--lav-text)}
.see-more{left:854px;top:70px;color:var(--primary);text-align:center}
.see-more b{display:block;font-size:32px;font-weight:700}
.see-more small{font-size:15px;font-weight:700}

/* about */
.about-photo{left:117px;top:872px;width:475px;height:422px;border-radius:36px;background:linear-gradient(180deg,#ffffff 0%,#fbf3fb 27%,#e88ae6 28%,#b48cf0 65%,#7fa2f7 100%)}
.about-title{left:655px;top:884px;font-size:35px;line-height:40px;font-weight:700;color:var(--ink)}
.about-text{left:655px;top:985px;width:360px;font-size:14.5px;line-height:18px;color:#55525e}
.about-rule{left:655px;width:418px;height:1px;background:var(--line)}
.about-item{left:655px;font-size:16.5px;font-weight:700;color:var(--ink)}
.about-btn{left:655px;top:1226px;width:180px;height:50px}

/* team */
.team-bg{left:0;top:1396px;width:1200px;height:689px;background:var(--lilac-bg)}
.team-title{left:117px;top:1474px;font-size:34px;font-weight:700;color:var(--ink)}
.team-all{left:971px;top:1497px;font-size:18px;font-weight:700;color:var(--primary);border-bottom:2px solid var(--primary);padding-bottom:3px}
.card{top:1585px;width:312px;height:390px;background:var(--white);border:1px solid #ebe7f6;border-radius:14px;text-align:center}
.card.featured{box-shadow:0 10px 28px rgba(80,60,160,.14)}
.card .star{position:absolute;left:18px;top:16px;width:28px;height:28px}
.avatar{position:absolute;left:92px;top:50px;width:127px;height:127px;border-radius:50%}
.card h3{position:absolute;left:0;right:0;top:195px;font-size:20px;font-weight:400;color:var(--ink)}
.card .role{position:absolute;left:0;right:0;top:224px;font-size:15px;color:var(--muted)}
.card .mail{position:absolute;left:0;right:0;top:268px;font-size:15px;color:var(--link-blue)}
.card-btn{position:absolute;left:61px;top:310px;width:191px;height:44px;border:1.5px solid var(--primary);border-radius:6px;color:var(--primary);font-weight:700;font-size:15px;display:flex;align-items:center;justify-content:center}
.card.featured .card-btn{background:var(--primary);color:var(--white)}
.arrow{top:1750px;width:60px;height:60px;border-radius:50%;display:flex;align-items:center;justify-content:center}

/* booking */
.book-title{left:117px;top:2166px;font-size:34px;line-height:41px;font-weight:700;color:var(--ink)}
.label{left:117px;font-size:14.5px;color:var(--ink)}
.field{background:var(--field);border:1px solid #ece9f8;border-radius:6px;font-size:14.5px;color:#77737f;padding:16px 22px}
.check{display:flex;align-items:center;gap:14px;font-size:14.5px;color:var(--ink)}
.check i{width:22px;height:22px;border:1px solid #d8d4e6;border-radius:4px;background:var(--white)}
.submit{left:117px;top:2657px;width:639px;height:59px;font-size:15.5px}
.book-photo{left:771px;top:2275px;width:312px;height:441px;border-radius:18px;background:linear-gradient(180deg,#ee8fe7 0%,#c47ff0 55%,#8f62e6 100%)}

/* cta */
.cta-bg{left:0;top:2969px;width:1200px;height:540px;background:var(--lavender)}
.cta{left:117px;top:2821px;width:966px;height:278px;border-radius:36px;background:var(--primary);overflow:hidden}
.cta-arc{position:absolute;left:544px;top:-205px;width:422px;height:422px;border-radius:50%;background:var(--lilac-bg)}
.cta h2{position:absolute;left:94px;top:84px;font-size:33px;line-height:40px;font-weight:700;color:var(--white)}
.cta p{position:absolute;left:94px;top:178px;font-size:19px;color:#e6e0ff}
.cta-btn{position:absolute;left:666px;top:95px;width:180px;height:49px}

/* footer */
.foot-brand{left:122px;top:3182px}
.foot-text{left:117px;top:3254px;width:300px;font-size:16px;line-height:20px;color:#57545f}
.foot-col{top:3172px}
.foot-col h4{font-size:22px;font-weight:700;color:var(--ink);margin-bottom:22px}
.foot-col a{display:block;font-size:16px;color:#6d6a78;margin-bottom:20px}
.foot-rule{left:117px;top:3409px;width:966px;height:1px;background:#9994b0}
.copy{left:117px;top:3449px;font-size:16px;color:#57545f}
.social{top:3443px;width:25px;height:25px;border-radius:4px;background:#5a5766}
</style>
</head>
<body>

<!-- hero -->
<div class="abs hero-bg"></div>
<div class="abs deco-circle"></div>
<div class="abs brand" style="left:117px;top:31px"><span class="brand-dot"></span>Wellspring Crest</div>
<nav class="abs nav">
  <a class="active">Home</a><a>About</a><a>Meet The Team</a><a>Service</a><a>News</a><a>FAQs</a>
</nav>
<a class="abs btn nav-contact">Contact</a>

<h1 class="abs hero-title"><span>WELLSPRING</span><br>CREST PARTNERS</h1>
<p class="abs hero-text">Contrary to popular belief, Lorem Ipsum is not simply random text. It has roots in a piece of classical Latin</p>
<a class="abs btn hero-btn">Make Appointment</a>
<div class="abs hero-photo" role="img" aria-label="Photo of a smiling doctor in a white coat with a stethoscope"></div>

<section class="abs services">
  <h2>Healt Services For You</h2>
  <p>Contrary to popular belief, Lorem Ipsum is not simply random text. It has roots in a piece of classical.</p>
  <div class="abs tile tile-prep">
    <svg viewBox="0 0 44 44" fill="none" stroke="currentColor" stroke-width="2"><rect x="6" y="16" width="32" height="12" rx="6" transform="rotate(-45 22 22)"/><line x1="16" y1="16" x2="28" y2="28"/></svg>PrEP
  </div>
  <div class="abs tile tile-hep">
    <svg viewBox="0 0 44 44" fill="none" stroke="currentColor" stroke-width="2"><path d="M8 20c0-6 8-8 14-6 6 2 14 0 14-6v12c0 10-10 18-20 18-6 0-8-8-8-18z"/><path d="M22 14v10"/></svg>Hepatitis C
  </div>
  <div class="abs tile tile-hiv">
    <svg viewBox="0 0 44 44" fill="none" stroke="currentColor" stroke-width="2"><path d="M12 6l16 26M28 6L12 32"/><rect x="26" y="24" width="14" height="14" rx="3"/><path d="M33 28v6M30 31h6"/></svg>HIV
  </div>
  <div class="abs see-more"><b>+5</b><small>See All ›</small></div>
</section>

<!-- about -->
<div class="abs about-photo" role="img" aria-label="Photo of three smiling medical staff in coats and scrubs"></div>
<h2 class="abs about-title">Easy way to healt<br>consultation</h2>
<p class="abs about-text">There are many variations of passages of Lorem Ipsum available, but the majority have suffered alteration in some form, by injected humour,</p>
<div class="abs about-rule" style="top:1083px"></div>
<div class="abs about-item" style="top:1095px">Primary Care</div>
<div class="abs about-rule" style="top:1132px"></div>
<div class="abs about-item" style="top:1145px">Urgent Care</div>
<a class="abs btn about-btn">More About Us</a>

<!-- team -->
<div class="abs team-bg"></div>
<h2 class="abs team-title">MEET THE TEAM</h2>
<a class="abs team-all">See All Teams</a>

<article class="abs card" style="left:117px">
  <svg class="star" viewBox="0 0 24 24"><path fill="#f0524a" d="M12 2l2.9 6.6 7.1.6-5.4 4.7 1.6 7L12 17.3 5.8 21l1.6-7L2 9.2l7.1-.6z"/></svg>
  <div class="avatar" role="img" aria-label="Portrait of doctor" style="background:#f2c2ee"></div>
  <h3>Dr. Mara Ellison</h3><div class="role">Radiology</div><div class="mail">mara@email.com</div>
  <a class="card-btn">Make Appoinment</a>
</article>
<article class="abs card featured" style="left:444px">
  <svg class="star" viewBox="0 0 24 24"><path fill="#f0524a" d="M12 2l2.9 6.6 7.1.6-5.4 4.7 1.6 7L12 17.3 5.8 21l1.6-7L2 9.2l7.1-.6z"/></svg>
  <div class="avatar" role="img" aria-label="Portrait of doctor" style="background:#f9c6c4"></div>
  <h3>Dr. Mara Ellison</h3><div class="role">Radiology</div><div class="mail">mara@email.com</div>
  <a class="card-btn">Make Appoinment</a>
</article>
<article class="abs card" style="left:771px">
  <svg class="star" viewBox="0 0 24 24"><path fill="#f0524a" d="M12 2l2.9 6.6 7.1.6-5.4 4.7 1.6 7L12 17.3 5.8 21l1.6-7L2 9.2l7.1-.6z"/></svg>
  <div class="avatar" role="img" aria-label="Portrait of doctor" style="background:#dccaf7"></div>
  <h3>Dr. Mara Ellison</h3><div class="role">Radiology</div><div class="mail">mara@email.com</div>
  <a class="card-btn">Make Appoinment</a>
</article>
<div class="abs arrow" style="left:86px;background:#d6cbf6"><svg width="22" height="22" viewBox="0 0 22 22"><path d="M14 3l-8 8 8 8" fill="none" stroke="#fff" stroke-width="3"/></svg></div>
<div class="abs arrow" style="left:1054px;background:#a98ceb"><svg width="22" height="22" viewBox="0 0 22 22"><path d="M8 3l8 8-8 8" fill="none" stroke="#fff" stroke-width="3"/></svg></div>

<!-- booking -->
<h2 class="abs book-title">Now Booking For TeleHealth &amp;<br>In-Person Appointments</h2>
<div class="abs label" style="top:2275px">Fill out the form to make an appointment</div>
<div class="abs field" style="left:117px;top:2313px;width:639px;height:47px">Fullname</div>
<div class="abs field" style="left:117px;top:2381px;width:312px;height:46px">Phone Number</div>
<div class="abs field" style="left:443px;top:2381px;width:313px;height:46px">Email</div>
<div class="abs label" style="top:2448px">What are you inquiring about?</div>
<div class="abs field" style="left:117px;top:2475px;width:639px;height:122px">Additional Info</div>
<div class="abs check" style="left:117px;top:2616px"><i></i>In - Person</div>
<div class="abs check" style="left:258px;top:2616px"><i></i>Telehealth</div>
<a class="abs btn submit">SUBMIT</a>
<div class="abs book-photo" role="img" aria-label="Photo of a smiling doctor with arms crossed"></div>

<!-- cta -->
<div class="abs cta-bg"></div>
<section class="abs cta">
  <div class="cta-arc"></div>
  <h2>Want to make an<br>appointment easily ?</h2>
  <p>You can get to doing things you love.</p>
  <a class="btn cta-btn">Contact Here</a>
</section>

<!-- footer -->
<div class="abs brand foot-brand"><span class="brand-dot"></span>Wellspring Crest</div>
<p class="abs foot-text">Contrary to popular belief, Lorem Ipsum is not simply random text. It has roots in a piece of classical Latin</p>
<div class="abs foot-col" style="left:546px"><h4>Services</h4><a>PrEP</a><a>Hepatitis C</a><a>HIV</a><a>See All Sevices</a></div>
<div class="abs foot-col" style="left:772px"><h4>About</h4><a>Our Story</a><a>Benefits</a><a>Teams</a><a>Careers</a></div>
<div class="abs foot-col" style="left:962px"><h4>Help</h4><a>FAQS</a><a>Contact</a></div>
<div class="abs foot-rule"></div>
<div class="abs copy">Copyright 2022 Wellspring Crest Partners | All Right Reserved</div>
<div class="abs social" style="left:962px"></div>
<div class="abs social" style="left:1009px"></div>
<div class="abs social" style="left:1058px"></div>

</body>
</html>
```